New Subscription Box business needs a Mailer Box design

We need you to take our existing logo and recreate it to make an awesome mailer box.
The new business is a subscription book box aimed at 0-8yr olds.
Design needs -
We are limited to a single print colour which should be a strong green or orange, the second colour will be the brown box itself. we want the design to be on all external box surfaces.
top surface - main design space logo and name
front edge - website (tallowreadcrate.com.au)
back edge - quote of some sort (to be advised)
side edge 1 - photoreel
side edge 2 - friendwall
bottom (underneath) - game board (i.e. snakes n ladders, or checkers or ?).
The recreated logo would also be used in website / photoreel / friendwall marketing.
The current logo needs the name changed from marlow little reeds to tallow read crate.
We also need a window on the top of the box for the courier label. This needs to fit a sticker of '150x100mm'.
the box is 340 x 290 x 80mm
Target Market(s)
parents, grandparents, family members, friends with children aged 0-8

```html
<!DOCTYPE html>
<html lang="en">
<head>
<meta charset="utf-8">
<title>Tallow Read Crate – Mailer Box Package Design</title>
<link rel="stylesheet" href="https://fonts.googleapis.com/css2?family=Varela+Round&family=Montserrat:wght@500&family=Arimo:ital@0;1&display=swap">
<style>
  :root {
    --stage: #6c6c6c;
    --stage-light: #8a8a8a;
    --print-orange: #f06b3e;
    --print-orange-edge: #c6522c;
    --kraft: #cd9b6a;
    --caption-white: #f2f2f2;
  }
  * { box-sizing: border-box; margin: 0; padding: 0; }
  html, body { width: 1200px; height: 960px; overflow: hidden; }
  body {
    background: radial-gradient(circle at 85% 20%, var(--stage-light), var(--stage) 60%);
    position: relative;
    font-family: "Varela Round", sans-serif;
  }
  .presentation-title {
    position: absolute; left: 20px; top: 60px; width: 300px; text-align: center;
  }
  .presentation-title .brand-name {
    display: block; font-family: "Varela Round", sans-serif; white-space: nowrap;
    color: var(--kraft); font-size: 30px; line-height: 1.2;
  }
  .presentation-title .caption {
    display: block; margin-top: 30px; font-family: "Montserrat", sans-serif;
    font-weight: 500; font-size: 20px; letter-spacing: 1px; color: var(--caption-white);
  }
  .box-net { position: absolute; left: 420px; top: 250px; width: 672px; height: 592px; }
  .panel { position: absolute; }
  .side-edge {
    left: 0; top: 0; width: 128px; height: 464px; background: var(--print-orange-edge);
    display: flex; align-items: center; justify-content: center;
  }
  .side-edge .social {
    transform: rotate(-90deg); white-space: nowrap; display: flex; align-items: center; gap: 12px;
    font-family: "Arimo", sans-serif; font-size: 15px; color: var(--kraft);
  }
  .social .icon-square { width: 26px; height: 26px; background: var(--kraft); border-radius: 3px; }
  .top-panel {
    left: 128px; top: 0; width: 544px; height: 464px; background: var(--print-orange);
  }
  .top-panel .box-brand {
    position: absolute; left: 0; right: 0; top: 110px; text-align: center; white-space: nowrap;
    font-size: 40px; color: var(--kraft);
  }
  .top-panel .label-window {
    position: absolute; right: 36px; bottom: 36px; width: 240px; height: 160px;
    background: var(--kraft); border-radius: 28px;
  }
  .front-edge {
    left: 128px; top: 464px; width: 544px; height: 128px; background: var(--kraft);
    display: flex; align-items: center; justify-content: center;
  }
  .front-edge .website {
    font-family: "Arimo", sans-serif; font-style: italic; font-size: 30px; white-space: nowrap;
    color: var(--print-orange);
  }
</style>
</head>
<body>
  <header class="presentation-title">
    <span class="brand-name">marlow little reeds</span>
    <span class="caption">PACKAGE DESIGN</span>
  </header>

  <main class="box-net">
    <section class="panel side-edge">
      <div class="social">
        <span class="icon-square" aria-hidden="true"></span>
        <span>www.friendwall.com/tallowreadcrate</span>
      </div>
    </section>
    <section class="panel top-panel">
      <div class="box-brand">tallow read crate</div>
      <div class="label-window" aria-label="Courier label window 150 x 100 mm"></div>
    </section>
    <section class="panel front-edge">
      <span class="website">www.tallowreadcrate.com.au</span>
    </section>
  </main>
</body>
</html>
```